Create a hull decoration for a racing sailboat

The graphics is for my racing sailboat i'm going to refit. I'm using for regata and it is visible to a lot of people in the see. I like the name "tidewren" and I would like some decoration that remember it. Decoration should very simple, few colours and soft. Since the final work will be printed and cut on plastic, simple drawing is welcome and the white of the hull should not be changed.

Colors

Requirements
Must have
• A logo that remember the name of the boat "Tidewren"
Nice to have
• The name of the boat should remain as in the photo, not a lot of colours should be used.
Should not have
• aggressive design and "strong colours", all should be simple, excential and soft

```html
<!DOCTYPE html>
<html lang="en">
<head>
<meta charset="utf-8">
<title>Tidewren hull decoration</title>
<link href="https://fonts.googleapis.com/css2?family=Arizonia&display=swap" rel="stylesheet">
<style>
  :root {
    --hull-white: #ffffff;
    --cut-line: #3fa9f5;
    --soft-amber: #f9b03b;
    --deep-amber: #f7941d;
    --pale-amber: #fcd79a;
    --name-ink: #3a0a10;
  }
  html, body {
    margin: 0;
    padding: 0;
    overflow: hidden;
    background: var(--hull-white);
  }
  .hull-decal {
    position: relative;
    width: 1200px;
    height: 300px;
    overflow: hidden;
    background: var(--hull-white);
  }
  .hull-decal__art {
    position: absolute;
    inset: 0;
    width: 1200px;
    height: 300px;
  }
  .cut-outline {
    fill: none;
    stroke: var(--cut-line);
    stroke-width: 0.8;
    stroke-dasharray: 6 4;
  }
  .wake-artwork {
    fill: url(#wakeTone);
  }
  .boat-name {
    position: absolute;
    left: 138px;
    top: 104px;
    margin: 0;
    font-family: "Arizonia", cursive;
    font-weight: 400;
    font-size: 50px;
    line-height: 1;
    color: var(--name-ink);
  }
</style>
</head>
<body>
  <div class="hull-decal">
    <svg class="hull-decal__art" viewBox="0 0 1200 300">
      <defs>
        <linearGradient id="wakeTone" x1="0" y1="0" x2="1" y2="0">
          <stop offset="0" stop-color="var(--pale-amber)"/>
          <stop offset="0.6" stop-color="var(--soft-amber)"/>
          <stop offset="1" stop-color="var(--deep-amber)"/>
        </linearGradient>
      </defs>
      <path class="cut-outline" aria-hidden="true"
            d="M75 80 Q560 120 1184 62 L1162 198 Q560 285 27 202 Z"/>
      <path class="wake-artwork" role="img"
            aria-label="Amber wake artwork: flowing streaks sweeping into curved arcs with small stars at the bow end"
            d="M90 168 Q600 200 960 140 Q1010 105 1120 100 L1110 185 Q1000 215 600 222 Q300 222 90 178 Z"/>
    </svg>
    <p class="boat-name">Tidewren</p>
  </div>
</body>
</html>
```